Business Card Design

We are a new residential construction company.our team is made up of young highly skilled tradesman of the next generation of carpenters coming through with new skills and ideas.we chose the name meridian as it means strikingly different from the rest as this is what we plan to be and we would like to portray this in our business card.we like Bold lettering as we want to make a statement, also the use of colour would be great as we want to stand out from the usual plain construction cards and logos.
I have attached a logo sketch I did as a rough idea if you can tidy it up or improve on it would be good.
I have also attached the LBP logo please include this on the card small but still legible.
open to any colourschemes ideas.
thanks
(note)please delete the LBP#804317 off from the card details please.
Industry/Entity Type
Construction
Contact Information for Business Card
MERIDIAN CONSTRUCTION LIMITED
Director:Tom Halvick
Mobile :0217364820
Email:Meridian.Construction@quillpost.example
Address:48 Wendle place,Ashgrove park 2091,Auckland
LBP#BP804317

```html
<!DOCTYPE html>
<html lang="en">
<head>
<meta charset="utf-8">
<title>Meridian Construction – Business Card</title>
<link rel="stylesheet" href="https://fonts.googleapis.com/css2?family=Source+Sans+3:wght@400;700&display=swap">
<style>
  :root {
    --backdrop: #5a5049;
    --card: #221f20;
    --ink: #ffffff;
    --accent: #4a5bc4;
    --accent-deep: #2f3c9a;
    --shine: #e8ecff;
  }
  * { box-sizing: border-box; margin: 0; padding: 0; }
  html, body {
    width: 1200px; height: 1000px; overflow: hidden;
    background: var(--backdrop);
    font-family: "Source Sans 3", "Myriad Pro", sans-serif;
    color: var(--ink);
  }
  .canvas { position: relative; width: 1200px; height: 1000px; }
  .card {
    position: absolute; width: 700px; height: 400px;
    background: var(--card);
    box-shadow: 0 10px 30px rgba(0,0,0,.35);
    overflow: hidden;
  }
  .card--front { left: 250px; top: 60px; }
  .card--back { left: 250px; top: 540px; }

  .stripe {
    position: absolute; height: 7px;
    background: linear-gradient(90deg, var(--accent-deep) 0%, var(--accent) 35%, var(--shine) 50%, var(--accent) 65%, var(--accent-deep) 100%);
  }
  .card--front .stripe { left: 0; right: 0; top: 300px; }

  .brand { position: absolute; display: flex; align-items: center; gap: 12px; font-weight: 700; color: var(--ink); text-transform: uppercase; }
  .brand__mark { background: var(--accent); }
  .card--front .brand { left: 150px; top: 130px; }
  .card--front .brand__mark { width: 22px; height: 22px; }
  .card--front .brand__name { font-size: 38px; line-height: 1.05; letter-spacing: 1px; }
  .card--back .brand { left: 60px; top: 42px; gap: 8px; }
  .card--back .brand__mark { width: 12px; height: 12px; }
  .card--back .brand__name { font-size: 20px; line-height: 1.05; letter-spacing: .5px; }

  .stripe--left { left: 0; width: 95px; top: 150px; }
  .stripe--right { right: 0; width: 150px; top: 214px; }

  .identity { position: absolute; left: 110px; top: 140px; text-align: right; width: 440px; }
  .identity__company { font-size: 25px; line-height: 1.1; }
  .identity__role { font-size: 28px; line-height: 1.15; }
  .identity__label { color: var(--accent); }

  .badge { position: absolute; right: 40px; top: 80px; width: 56px; height: 56px; background: #fff; border-radius: 2px; }

  .contacts { position: absolute; left: 40px; top: 268px; list-style: none; font-size: 17px; line-height: 1.45; }
  .contacts li { display: flex; align-items: center; gap: 8px; }
  .contacts svg { width: 14px; height: 14px; stroke: var(--accent); fill: none; stroke-width: 1.6; }

  .address { position: absolute; right: 40px; top: 262px; text-align: right; font-style: normal; font-size: 19px; line-height: 1.2; }
  .address__label { color: var(--accent); }
</style>
</head>
<body>
<main class="canvas">
  <section class="card card--front" aria-label="Card front">
    <div class="brand">
      <span class="brand__mark"></span>
      <span class="brand__name">Meridian<br>Construction</span>
    </div>
    <div class="stripe"></div>
  </section>

  <section class="card card--back" aria-label="Card back">
    <div class="brand">
      <span class="brand__mark"></span>
      <span class="brand__name">Meridian<br>Construction</span>
    </div>
    <div class="stripe stripe--left"></div>
    <div class="identity">
      <p class="identity__company">MERIDIAN CONSTRUCTION LIMITED</p>
      <p class="identity__role"><span class="identity__label">Director:</span>Tom Halvick</p>
    </div>
    <div class="stripe stripe--right"></div>
    <div class="badge" role="img" aria-label="Licensed building practitioner badge"></div>

    <ul class="contacts">
      <li>
        <svg viewBox="0 0 14 14" aria-hidden="true"><rect x="3.5" y="1" width="7" height="12" rx="1.2"/><line x1="6" y1="11" x2="8" y2="11"/></svg>
        0217364820
      </li>
      <li>
        <svg viewBox="0 0 14 14" aria-hidden="true"><rect x="1" y="3" width="12" height="8"/><polyline points="1,3 7,8 13,3"/></svg>
        Meridian.Construction@quillpost.example
      </li>
    </ul>

    <address class="address">
      <span class="address__label">Address</span><br>
      48 Wendle place,<br>
      Ashgrove park 2091,<br>
      Auckland LBP#BP804317
    </address>
  </section>
</main>
</body>
</html>
```